MO&A - Business Card and Stationery for a Law Firm
Mendívil Ortuzar & Asociados
Professional
Julián Esteban Mendívil Ortuzar
Abogado
Carrera 48 No. 62-14 Of. 305
Bogotá D.C., Colombia
julian.mendivil@mendivilortuzar.com
www.mendivilortuzar.com
The text on the back of the card is in Spanish, for your information the meaning in English is as follows:
Companies in Colombia and abroad.
International business.
Tax planning.
Foreign investments.
Inmigration.
Industrial property.
Please distribute the text as you consider.
Logo and the following text:
Sociedades en Colombia y el exterior.
Negocios internacionales.
Planeación tributaria.
Inversión extranjera.
Asuntos migratorios.
Propiedad Industrial.

```html
<!DOCTYPE html>
<html lang="es">
<head>
<meta charset="utf-8">
<title>Mendívil Ortuzar &amp; Asociados – Tarjeta</title>
<link rel="stylesheet" href="https://fonts.googleapis.com/css2?family=Cinzel:wght@400;500&family=Tinos&display=swap">
<style>
  :root{
    --navy:#14284a;
    --ink:#1c2b45;
    --grey:#8a8f97;
    --rule:#c9ccd1;
    --paper:#ffffff;
    --backdrop:#e8e6e2;
  }
  *{margin:0;padding:0;box-sizing:border-box}
  html,body{width:1200px;height:778px;overflow:hidden;background:var(--backdrop)}
  .card{
    position:absolute;left:60px;top:73px;width:1080px;height:632px;
    background:var(--paper);box-shadow:0 4px 18px rgba(0,0,0,.18);
  }
  .tab{position:absolute;top:174px;width:26px;height:195px;background:var(--navy)}
  .tab--left{left:0;border-radius:0 22px 22px 0}
  .tab--right{right:0;border-radius:22px 0 0 22px}
  .brand{position:absolute;left:225px;top:105px;display:flex;align-items:center;gap:28px}
  .brand__square{width:100px;height:100px;background:var(--navy)}
  .brand__name{
    font-family:"Cinzel",serif;font-weight:400;color:var(--navy);
    font-size:52px;line-height:1.05;letter-spacing:1px;
  }
  .holder{position:absolute;right:560px;top:408px;text-align:right;font-family:"Cinzel",serif}
  .holder__name{font-size:25px;color:var(--ink);letter-spacing:.5px;font-weight:400}
  .holder__role{font-size:17px;color:var(--grey);margin-top:6px;letter-spacing:1px}
  .divider{position:absolute;left:540px;top:324px;width:1px;height:240px;background:var(--rule)}
  .contact{
    position:absolute;left:579px;top:332px;list-style:none;
    font-family:"Tinos",serif;font-size:23px;color:var(--ink);line-height:38px;
  }
  .contact li{display:flex;align-items:center;gap:12px}
  .contact svg{width:18px;height:18px;flex:none;fill:var(--grey)}
  .contact .plain{padding-left:0}
</style>
</head>
<body>
  <div class="card">
    <div class="tab tab--left"></div>
    <div class="tab tab--right"></div>

    <div class="brand">
      <div class="brand__square"></div>
      <div class="brand__name">Mendívil Ortuzar<br>&amp; Asociados</div>
    </div>

    <div class="holder">
      <p class="holder__name">Julián Esteban Mendívil Ortuzar</p>
      <p class="holder__role">Abogado</p>
    </div>

    <div class="divider"></div>

    <ul class="contact">
      <li>Carrera 48 No. 62-14 Of. 305</li>
      <li>Bogotá D.C., Colombia</li>
      <li><svg viewBox="0 0 24 24"><path d="M6.6 10.8a15 15 0 0 0 6.6 6.6l2.2-2.2c.3-.3.7-.4 1-.2 1.1.4 2.3.6 3.6.6.6 0 1 .4 1 1V20c0 .6-.4 1-1 1A17 17 0 0 1 3 4c0-.6.4-1 1-1h3.5c.6 0 1 .4 1 1 0 1.3.2 2.5.6 3.6.1.3 0 .7-.2 1z"/></svg>+57 (1) 4390276</li>
      <li><svg viewBox="0 0 24 24"><path d="M8 1h8a2 2 0 0 1 2 2v18a2 2 0 0 1-2 2H8a2 2 0 0 1-2-2V3a2 2 0 0 1 2-2zm0 3v14h8V4zm4 15.5a1 1 0 1 0 0 2 1 1 0 0 0 0-2z"/></svg>+57 3154027719</li>
      <li><svg viewBox="0 0 24 24"><path d="M2 5h20v14H2zm2 2v.5l8 5.5 8-5.5V7zm0 2.9V17h16V9.9l-8 5.5z"/></svg>julian.mendivil@mendivilortuzar.com</li>
      <li><svg viewBox="0 0 24 24"><path d="M12 2a10 10 0 1 0 0 20 10 10 0 0 0 0-20zm6.9 9h-3a15 15 0 0 0-1.3-6A8 8 0 0 1 18.9 11zM12 4c.9 1.2 1.7 3.6 1.9 7h-3.8c.2-3.4 1-5.8 1.9-7zM9.4 5a15 15 0 0 0-1.3 6h-3A8 8 0 0 1 9.4 5zM5.1 13h3a15 15 0 0 0 1.3 6A8 8 0 0 1 5.1 13zm6.9 7c-.9-1.2-1.7-3.6-1.9-7h3.8c-.2 3.4-1 5.8-1.9 7zm2.6-1a15 15 0 0 0 1.3-6h3a8 8 0 0 1-4.3 6z"/></svg>www.mendivilortuzar.com</li>
    </ul>
  </div>
</body>
</html>
```